Electrical contractor

looking for a standard sized, horizontal, double sided business card for an electrical contractors business.
i have played around on microsoft word (only computer program i know how to use!) and will attach what i have made so far, really open to any ideas. i just want the DORB to stand out to the rest of the business name.

i wish to use the colours black and green, and white for writing. i will attach the pictures i took off google, i want to either use them, or somethin similar for the back grounds

i wish the front to have the following info:
business name: D.O.R.B ELECTRICAL CONTRACTORS
MY NAME; CORBIN HOLT
STATUS; A CLASS ELECTRICIAN
LICENSE NO; TRN517394
PH NO. 0431576204
EMAIL ADD. DORB.ELECTRICAL@VELTOMAIL.COM
AND MY SLOGAN: where excellence meets integrity, and service comes with a smile.

i am not sure what to have on the back, other than what i do for work.eg titled WHAT WE DO
i dont want too much written on there or will look crowded, but options to add to back, from most important to least, please pick however many you think will look the best
new homes/extentions
led lighting and downlights
Solar Power
power
safety switches
switchboards
telephone and tv
smoke alarms
stoves and ovens
hot water systems
fault finding
re wiring
Updates

Thank you to those who have submitted designs, I would like to change my slogan to something more simple, I'm thinking something like. RELIABLE. EFFICIENT. PROFESSIONAL. AFFORDABLE. in what ever order you thinks fits best. Thanks

Industry/Entity Type

Contractor

```html
<!DOCTYPE html>
<html lang="en">
<head>
<meta charset="utf-8">
<title>D.O.R.B. Electrical Contractors – Business Card</title>
<link rel="stylesheet" href="https://fonts.googleapis.com/css2?family=Exo+2:wght@300;400;500&display=swap">
<style>
  :root {
    --stage: #e4e4e4;
    --card: #1f1f1f;
    --green: #3fa845;
    --white: #f2f2f2;
    --muted: #c9c9c9;
    --faint: #2c2c2c;
  }
  * { margin: 0; padding: 0; box-sizing: border-box; }
  html, body { width: 1200px; height: 997px; overflow: hidden; }
  body {
    background: var(--stage);
    font-family: "Exo 2", "Helvetica Neue", Arial, sans-serif;
    color: var(--white);
    position: relative;
  }
  .card {
    position: absolute;
    top: 350px;
    width: 520px;
    height: 300px;
    background: var(--card);
    border-radius: 3px;
    box-shadow: 0 10px 28px rgba(0,0,0,0.25);
    overflow: hidden;
  }
  .card--front { left: 60px; }
  .card--back { left: 620px; }

  .front__glow {
    position: absolute;
    right: 60px;
    top: 30px;
    width: 170px;
    height: 170px;
    border-radius: 50%;
    border: 14px solid var(--faint);
  }
  .brand { position: absolute; left: 30px; top: 28px; }
  .brand__name {
    font-size: 46px;
    font-weight: 400;
    letter-spacing: 3px;
    color: var(--green);
    line-height: 1;
  }
  .brand__trade {
    font-size: 20px;
    font-weight: 300;
    color: var(--white);
    margin-top: 2px;
  }
  .person { position: absolute; left: 30px; top: 150px; }
  .person__name {
    font-size: 17px;
    font-weight: 400;
    letter-spacing: 1px;
    color: var(--muted);
  }
  .person__name span { color: var(--green); }
  .person__meta {
    font-size: 9px;
    font-weight: 300;
    color: var(--muted);
    line-height: 1.2;
    margin-top: 1px;
  }
  .contact {
    position: absolute;
    left: 30px;
    top: 214px;
    font-size: 12px;
    font-weight: 300;
    line-height: 1.4;
    color: var(--white);
  }
  .contact dt { display: inline-block; width: 48px; }
  .contact dd { display: inline; }
  .slogan {
    position: absolute;
    right: 30px;
    bottom: 22px;
    font-size: 12px;
    font-style: italic;
    font-weight: 300;
    color: var(--white);
  }

  .services {
    position: absolute;
    left: 0; right: 0;
    top: 48px;
    text-align: center;
    font-size: 13px;
    font-weight: 300;
    line-height: 1.55;
    color: var(--white);
  }
  .mark {
    position: absolute;
    left: 0; right: 0;
    top: 170px;
    display: flex;
    justify-content: center;
    align-items: center;
    gap: 12px;
  }
  .mark__dot {
    width: 22px;
    height: 22px;
    border-radius: 50%;
    background: var(--green);
  }
  .mark__name {
    font-size: 34px;
    font-weight: 400;
    letter-spacing: 3px;
    color: var(--green);
  }
</style>
</head>
<body>

  <section class="card card--front" aria-label="Business card front">
    <div class="front__glow" aria-hidden="true"></div>
    <header class="brand">
      <h1 class="brand__name">D.O.R.B.</h1>
      <p class="brand__trade">Electrical Contractors</p>
    </header>
    <div class="person">
      <p class="person__name">CORBIN<span>HOLT</span></p>
      <p class="person__meta">A Class Electrician<br>LIC.NO: trn517394</p>
    </div>
    <dl class="contact">
      <div><dt>phone:</dt><dd>0431576204</dd></div>
      <div><dt>email:</dt><dd>dorb.electrical@veltomail.com</dd></div>
    </dl>
    <p class="slogan">“Where excellence meets integrity and service comes with a smile”</p>
  </section>

  <section class="card card--back" aria-label="Business card back">
    <p class="services">
      New homes/extentions | Led lighting and downlights | Solar Power | Power<br>
      Safety switches | Switchboards | Telephone and TV | Smoke alarms<br>
      Stoves and ovens | Hot water systems | Fault finding | Re wiring
    </p>
    <div class="mark">
      <span class="mark__dot" aria-hidden="true"></span>
      <span class="mark__name">DORB</span>
    </div>
  </section>

</body>
</html>
```